Prospectus/Brochure Design for Partnerships Proposal

Require prospectus to be designed for partnerships packages with our company. The goal of this prospectus is to inspire partners to join Vintrel (our company).

Design should be creative and include colour and visual elements to make engaging.

Creativity with layout is encouraged as you see fit.

Company is Vintrel.com.au

Contents of brocuhure/prospectus in .pdf. Layout ok to play around with.

Target Market(s)

Startup, Small Business

Industry/Entity Type

Startup

Font styles to use
Sans Serif

Colors

Designer to choose colors to be used in the design.

Requirements
Must have
• Well designed, colour, visual elements, consistency through design with regards to spacing, typography and design elements
Should not have
• Too many colours, select a creative colour pallete and stick with it. Clipart or non vector images.

```html
<!DOCTYPE html>
<html lang="en">
<head>
<meta charset="utf-8">
<title>Vintrel Prospectus</title>
<link href="https://fonts.googleapis.com/css2?family=Open+Sans:wght@400;600;700&display=swap" rel="stylesheet">
<style>
:root{
  --backdrop:#fdf0cf;
  --paper:#ffffff;
  --ink:#222222;
  --ink-soft:#3a3a3a;
  --rule:#d8d8d8;
  --mauve:#8c7775;
  --band:rgba(120,100,98,.78);
  --photo-warm-a:#e8ddd2;
  --photo-warm-b:#b89a80;
  --photo-city-a:#b9aeae;
  --photo-city-b:#e4dede;
}
*{box-sizing:border-box;margin:0;padding:0}
html,body{width:1200px;height:900px;overflow:hidden}
body{background:var(--backdrop);font-family:"Open Sans",sans-serif;color:var(--ink);position:relative}
.page{position:absolute;top:77px;width:524px;height:678px;background:var(--paper);overflow:hidden}
.page--cover{left:64px}
.page--about{left:612px}
.page-footer{position:absolute;left:0;right:0;top:600px;height:78px;border-top:1px solid var(--rule);text-align:center;padding-top:22px;font-size:10.5px;color:var(--ink-soft)}

/* cover */
.cover-photo{position:absolute;background:linear-gradient(120deg,var(--photo-warm-a),var(--photo-warm-b))}
.cover-photo--top{left:36px;top:0;width:460px;height:245px;clip-path:polygon(18% 0,100% 0,100% 100%,0 100%)}
.cover-photo--bottom{left:340px;top:355px;width:184px;height:245px;clip-path:polygon(26% 0,100% 0,100% 100%,0 100%)}
.wordmark{position:absolute;left:44px;top:258px;font-size:60px;font-weight:700;letter-spacing:-1px;line-height:1;color:var(--ink)}
.tagline{position:absolute;left:110px;top:328px;font-size:12.5px;color:var(--ink-soft)}
.cover-intro{position:absolute;z-index:2;left:44px;top:407px;font-size:15px;line-height:1.36;color:var(--ink-soft)}
.cover-title{position:absolute;left:47px;top:548px;font-size:34px;font-weight:700;color:var(--ink)}

/* about */
.about-photo{position:absolute;left:0;top:0;width:524px;height:243px;background:linear-gradient(180deg,var(--photo-city-a),var(--photo-city-b))}
.about-strip{position:absolute;left:0;top:243px;width:524px;height:7px;background:var(--mauve)}
.about-band{position:absolute;left:0;top:53px;width:524px;height:31px;background:var(--band);color:#fff;font-weight:700;font-size:16.5px;text-align:right;padding:4px 48px 0 0}
.about-intro{position:absolute;left:36px;top:120px;width:452px;height:124px;background:rgba(255,255,255,.9);border-radius:6px 6px 0 0;padding:12px 13px 0 13px;font-size:10.4px;line-height:1.22;text-align:justify;hyphens:auto}
.about-intro p+p{margin-top:12px}
.brand-square{position:absolute;left:56px;top:270px;width:79px;height:79px;background:#2b2b2b;box-shadow:inset 0 0 0 3px #3d3d3d}
.pull-quote{position:absolute;left:140px;top:266px;width:330px;text-align:right;font-size:17px;font-weight:700;line-height:1.22;color:var(--ink);white-space:nowrap}
.about-body{position:absolute;left:49px;top:364px;width:426px;font-size:10.4px;line-height:1.22;text-align:justify;hyphens:auto;color:var(--ink)}
.about-body p+p{margin-top:12px}
</style>
</head>
<body>
<section class="page page--cover">
  <div class="cover-photo cover-photo--top" role="img" aria-label="Photo of business partners shaking hands across a meeting table"></div>
  <div class="wordmark">Vintrel</div>
  <div class="tagline">empower. achieve. succeed.</div>
  <div class="cover-photo cover-photo--bottom" role="img" aria-label="Photo of a smiling woman resting her chin on her hand in a meeting"></div>
  <p class="cover-intro">a co-working space for entrepreneurs<br>and start-up businesses in Sydney, Australia.<br>Since 2011</p>
  <h1 class="cover-title">Prospectus</h1>
  <footer class="page-footer">www.vintrel.com.au</footer>
</section>

<section class="page page--about">
  <div class="about-photo" role="img" aria-label="Photo of a bright office interior with a city skyline view"></div>
  <h2 class="about-band">Who is Vintrel?</h2>
  <div class="about-intro">
    <p>Vintrel was started by Marcus Hollander and Daniel Hollander in 2011 with one main goal, to support entrepreneurs on their journey to success, to our knowledge we were the second coworking space to open in Sydney.</p>
    <p>With our optimistic view of business, we took on a 250sqm property @ 27 Loftus street Surry hills and started renovating. Day and night we put our blood sweat and tears into painting walls, laying floors, running wires, assembling furniture and erecting walls, meanwhile we put together our branding and digital presence.</p>
  </div>
  <div class="about-strip"></div>
  <div class="brand-square"></div>
  <blockquote class="pull-quote">“growing rapidly as it continues to<br>move towards its plans of dominating<br>the coworking sector, first in<br>Australia and then worldwide“</blockquote>
  <div class="about-body">
    <p>Two months later we opened our doors! With limited marketing knowledge our desks remained empty. It was the realization of the power of community that got us to where we are today.</p>
    <p>Vintrel starting creating events targeted at helping everyday people builds businesses and take control of the lives, since then we have quadrupled in size, we are now situated on 8 Harwood street in Surry hills with over 150 members and reaching over 30000 business owners and entrepreneurs Australia wide.</p>
    <p>Vintrel holds weekly events assisting and supporting entrepreneurs in their pursuit of running successful business all the while our niche and unbreakable community continues to thrive.</p>
    <p>Vintrel is growing rapidly as it continues to move towards its plans of dominating the coworking sector, first in Australia and then worldwide.</p>
  </div>
  <footer class="page-footer">www.vintrel.com.au</footer>
</section>
</body>
</html>
```